Business Card Design

I would like a new business card for my business Drive Haven, we operate within the automotive industry and offer customer retention solutions for independent mechanical workshops across Australia and New Zealand. The program incorporates service reminders and roadside assistance for consumers and is designed to get the client back for their vehicle service visit, I would like a doubled sided design that incorporates my logos and a two tone type card that has white and a carbon fibre look also use the blue in the logo I have uploaded. It would be great to have icons as the phone/fax/email etc details for the card are below. The finished design must be a print ready file useable.It would be great if the design could communicate the what type of business we are
Marcus Trelby
General Manager
Drive Haven Pty Ltd
Unit 5/42 Corrin Street
Wexmoor Newcastle NSW 2391
Ph:+61240173500
fax:+61240173600
Mobile:0415889214
Email:info@drivehaven-example.com.au
Updates
I have just upload a carbon fibre background for the business card hope it helps
Hello guys I am sorry fr no feedback I have been away over seas I will send feedback when I return monday
Industry/Entity Type
Automotive
Look and feel

```html
<!DOCTYPE html>
<html lang="en">
<head>
<meta charset="utf-8">
<title>Drive Haven Business Card</title>
<link href="https://fonts.googleapis.com/css2?family=Arimo:wght@400&display=swap" rel="stylesheet">
<style>
  :root {
    --brand-blue: #3aa3e0;
    --brand-blue-deep: #1f8fd4;
    --edge-grey: #c9d1d8;
    --card-white: #ffffff;
    --carbon-dark: #1c1d1f;
    --carbon-mid: #333538;
    --silver: #d6d9dd;
    --page-bg: #e9e7e3;
    --text-white: #ffffff;
  }
  * { box-sizing: border-box; margin: 0; padding: 0; }
  html, body {
    width: 1200px; height: 848px; overflow: hidden;
    background: var(--page-bg);
    font-family: "Arimo", Arial, sans-serif;
  }
  .canvas { position: relative; width: 1200px; height: 848px; }
  .card {
    position: absolute; top: 265px; width: 520px; height: 318px;
    overflow: hidden; box-shadow: 0 10px 28px rgba(0,0,0,0.25);
  }
  .card-front { left: 60px; background: var(--card-white); }
  .card-back { left: 620px; }
  .front-panel { position: absolute; inset: 0; }
  .front-brand {
    position: absolute; left: 30px; top: 109px; width: 240px;
    display: flex; align-items: center; gap: 12px;
  }
  .brand-dot {
    width: 34px; height: 34px; border-radius: 50%;
    background: var(--brand-blue); flex: none;
  }
  .brand-name {
    font-size: 30px; color: var(--brand-blue-deep); font-weight: 400;
    white-space: nowrap;
  }
  .contact {
    position: absolute; left: 338px; top: 34px; color: var(--text-white);
    font-size: 11.5px; line-height: 1.35;
  }
  .contact-name { font-size: 17px; line-height: 1.2; }
  .contact-role { font-size: 11.5px; margin-left: 8px; margin-bottom: 22px; }
  .contact-address { margin-bottom: 22px; }
  .contact-list { list-style: none; }
  .contact-list li { display: flex; align-items: center; gap: 7px; margin-bottom: 3px; }
  .contact-list svg { width: 11px; height: 11px; flex: none; fill: var(--text-white); }
  .carbon {
    position: absolute; inset: 0;
    background: radial-gradient(ellipse at 55% 40%, var(--carbon-mid), var(--carbon-dark) 75%);
  }
  .back-brand {
    position: absolute; left: 0; right: 0; top: 0; bottom: 0;
    display: flex; align-items: center; justify-content: center; gap: 16px;
  }
  .back-brand .brand-dot { width: 58px; height: 58px; }
  .back-brand .brand-name { font-size: 46px; color: var(--silver); }
</style>
</head>
<body>
<main class="canvas">

  <section class="card card-front" aria-label="Business card front">
    <svg class="front-panel" viewBox="0 0 520 318" preserveAspectRatio="none" aria-hidden="true">
      <path d="M296 0 Q246 160 318 318 L520 318 L520 0 Z" fill="var(--edge-grey)"/>
      <path d="M306 0 Q256 160 328 318 L520 318 L520 0 Z" fill="var(--brand-blue)"/>
    </svg>

    <div class="front-brand">
      <span class="brand-dot"></span>
      <span class="brand-name">Drive Haven</span>
    </div>

    <div class="contact">
      <p class="contact-name">Marcus Trelby</p>
      <p class="contact-role">General Manager</p>
      <p class="contact-address">Drive Haven Pty Ltd<br>Unit 5/42 Corrin Street<br>Wexmoor Newcastle NSW 2391</p>
      <ul class="contact-list">
        <li><svg viewBox="0 0 24 24" aria-label="Phone"><path d="M6.6 10.8a15 15 0 0 0 6.6 6.6l2.2-2.2a1 1 0 0 1 1-.25 11 11 0 0 0 3.6.6 1 1 0 0 1 1 1V20a1 1 0 0 1-1 1A17 17 0 0 1 3 4a1 1 0 0 1 1-1h3.5a1 1 0 0 1 1 1 11 11 0 0 0 .6 3.6 1 1 0 0 1-.25 1z"/></svg>+61240173500</li>
        <li><svg viewBox="0 0 24 24" aria-label="Mobile"><path d="M7 1h10a2 2 0 0 1 2 2v18a2 2 0 0 1-2 2H7a2 2 0 0 1-2-2V3a2 2 0 0 1 2-2zm0 3v14h10V4zm5 15.5a1 1 0 1 0 0 2 1 1 0 0 0 0-2z"/></svg>0415889214</li>
        <li><svg viewBox="0 0 24 24" aria-label="Fax"><path d="M7 2h8l3 3v4H7zM3 10h18a1 1 0 0 1 1 1v9a1 1 0 0 1-1 1H3a1 1 0 0 1-1-1v-9a1 1 0 0 1 1-1z"/></svg>+61240173600</li>
        <li><svg viewBox="0 0 24 24" aria-label="Email"><path d="M2 5h20v14H2zm2 2v.5l8 5 8-5V7l-8 5z"/></svg>info@drivehaven-example.com.au</li>
      </ul>
    </div>
  </section>

  <section class="card card-back" aria-label="Business card back">
    <div class="carbon" role="img" aria-label="Carbon fibre weave texture background"></div>
    <div class="back-brand">
      <span class="brand-dot"></span>
      <span class="brand-name">Drive Haven</span>
    </div>
  </section>

</main>
</body>
</html>
```